Design a powerpoint background using company logo/colours

We require a powerpoint background that incorporates our company colours and logo. I have attached the logo in various sizes.

Have fun and be imaginative

Our company colours are white and Red-236, Green-22 and Blue 86.
Please use these colours in designing the ppt background

Industry/Entity Type

It Company

Colors

Designer to choose colors to be used in the design.

```html
<!DOCTYPE html>
<html lang="en">
<head>
<meta charset="utf-8">
<title>Nodara – Presentation Background</title>
<link rel="stylesheet" href="https://fonts.googleapis.com/css2?family=Lora:ital,wght@0,700;1,700&display=swap">
<style>
  :root {
    --brand-red: #ec1656;
    --canvas-pink: #f7b8cb;
    --frame-light: #fbe3ea;
    --frame-deep: #ef6f98;
    --tagline-ink: #4a3a44;
    --white: #ffffff;
  }
  html, body {
    margin: 0;
    padding: 0;
    overflow: hidden;
  }
  body {
    width: 1200px;
    height: 900px;
  }
  .slide-background {
    position: relative;
    width: 1200px;
    height: 900px;
    background: var(--canvas-pink);
    overflow: hidden;
  }
  .tile-border {
    position: absolute;
    inset: 0;
    width: 1200px;
    height: 900px;
  }
  .brand-lockup {
    position: absolute;
    left: 88px;
    top: 72px;
    display: flex;
    align-items: center;
    gap: 16px;
  }
  .brand-name {
    font-family: "Lora", Georgia, serif;
    font-weight: 700;
    font-size: 78px;
    line-height: 1;
    color: var(--brand-red);
    letter-spacing: -1px;
  }
  .brand-mark {
    width: 58px;
    height: 58px;
    background: var(--brand-red);
  }
  .tagline {
    position: absolute;
    left: 0;
    right: 0;
    top: 770px;
    margin: 0;
    text-align: center;
    font-family: "Lora", Georgia, serif;
    font-style: italic;
    font-weight: 700;
    font-size: 56px;
    line-height: 1;
    color: var(--tagline-ink);
    letter-spacing: -0.5px;
    text-shadow: 2px 3px 3px rgba(60, 30, 45, 0.45);
  }
</style>
</head>
<body>
  <main class="slide-background">
    <svg class="tile-border" viewBox="0 0 1200 900" role="img"
         aria-label="Decorative border of white and red diamond tiles framing the slide">
      <defs>
        <linearGradient id="border-tone" x1="0" y1="0" x2="1" y2="1">
          <stop offset="0" stop-color="var(--frame-deep)" />
          <stop offset="0.5" stop-color="var(--frame-light)" />
          <stop offset="1" stop-color="var(--frame-deep)" />
        </linearGradient>
      </defs>
      <path fill="url(#border-tone)" fill-rule="evenodd"
            d="M0 0H1200V900H0Z M70 66V834H1130V66Z" />
    </svg>

    <div class="brand-lockup">
      <span class="brand-name">Nodara</span>
      <span class="brand-mark" aria-hidden="true"></span>
    </div>

    <p class="tagline">Tomorrow’s networks today</p>
  </main>
</body>
</html>
```